Lumora App | Pre-Launch Homepage

Dear designer,
Lumora is a soon to be launched innovative & free social platform for collaborative addictions quitting.
We require a design for our pre-launch homepage that will elevate our basic wireframes to the next level.
We would like the wireframes to serve as a guideline only, and not as a final version of the design. If you have cool ideas - we would appreciate your creativity!
* This is a pre-launch website for a mobile app, and as such the design must be consistent with the general style, design and atmosphere of the app (see screenshot in the shared Drive link).
* We liked the style and feel of the following website: http://palvexapp.com/ - Please let's use it as a reference as well.
* The existing text in the wireframes is there just to represent a place for text. Copy will be edited by us after the design is done.
Please find the wireframes attached, and all relevant design assets and app screenshots in the following Drive shared link -
https://files.norvakshare.com/open?id=7Q284KtP3mXcRf8Hj21W5vLzDne
Thanks,
Marcus
Industry/Entity Type
Social
Number of Pages Required
1 page
Look and feel
Each slider illustrates characteristics of the customer's brand and the style your logo design should communicate.

```html
<!DOCTYPE html>
<html lang="en">
<head>
<meta charset="utf-8">
<title>Lumora App | Pre-Launch Homepage</title>
<link href="https://fonts.googleapis.com/css2?family=Open+Sans:wght@300;400;600;700;800&display=swap" rel="stylesheet">
<style>
  :root {
    --yellow: #f6c500;
    --orange: #f39a1e;
    --dark: #2a2524;
    --dark-2: #3a302b;
    --ink: #3b3b3b;
    --muted: #7a7a7a;
    --white: #ffffff;
    --paper: #ffffff;
  }
  * { box-sizing: border-box; margin: 0; padding: 0; }
  html, body { width: 1200px; height: 3636px; overflow: hidden; }
  body { font-family: "Open Sans", Arial, sans-serif; color: var(--ink); background: var(--paper); position: relative; }
  section, header, footer { position: absolute; left: 0; width: 1200px; }
  .abs { position: absolute; }

  /* Hero */
  .hero { top: 0; height: 560px; overflow: hidden;
    background: linear-gradient(180deg, #5a3a22 0%, #b8682a 38%, #d78a34 55%, #7b4a26 80%, #3a2a22 100%); }
  .hero-photo { inset: 0; position: absolute;
    background: radial-gradient(ellipse 600px 220px at 560px 300px, rgba(255,196,90,.55), transparent 70%); }
  .brand { top: 28px; left: 0; width: 1200px; text-align: center; font-weight: 800; font-size: 52px; color: var(--yellow); letter-spacing: 1px; }
  .tagline { top: 100px; width: 1200px; text-align: center; color: var(--yellow); font-size: 20px; font-weight: 600; }
  .contact { top: 18px; left: 808px; display: flex; align-items: center; gap: 10px; color: var(--white); font-size: 14px; }
  .contact .dot { width: 30px; height: 30px; border-radius: 50%; background: #1c1a19; display: grid; place-items: center; }
  .menu-btn { top: 0; left: 1052px; width: 74px; height: 58px; background: var(--yellow); display: grid; place-items: center; }
  .hero-title { top: 272px; left: 76px; width: 620px; color: var(--white); font-size: 25px; font-weight: 700; line-height: 1.35; text-transform: uppercase; }
  .btn-subscribe { top: 384px; left: 92px; width: 112px; height: 40px; background: var(--yellow); color: var(--dark); font-size: 14px; border-radius: 3px; display: grid; place-items: center; }
  .hero-phone { top: 150px; left: 800px; width: 200px; height: 380px; border-radius: 28px; background: linear-gradient(160deg,#f4f4f4,#cfcfcf); }
  .hero-phone-2 { top: 200px; left: 900px; width: 170px; height: 330px; border-radius: 26px; background: linear-gradient(160deg,#2b2b2b,#0d0d0d); }
  .arrow { top: 290px; color: rgba(255,255,255,.85); }
  .dots { top: 520px; left: 550px; display: flex; gap: 10px; }
  .dots span { width: 30px; height: 30px; border-radius: 50%; background: rgba(255,255,255,.9); }

  /* Features band */
  .features { top: 560px; height: 500px; background: linear-gradient(180deg, #2c2624, #3b3029 60%, #4a3b30); }
  .feature { top: 120px; width: 300px; text-align: center; }
  .feature .icon { width: 110px; height: 110px; margin: 0 auto 24px; display: grid; place-items: center; }
  .feature h3 { font-size: 16px; font-weight: 400; color: var(--white); margin-bottom: 10px; }
  .feature h3.accent { color: var(--yellow); }
  .feature p { font-size: 15px; color: #e8e0da; line-height: 1.45; }

  /* Split sections */
  .fun { top: 1060px; height: 480px; background: var(--paper); }
  .inspire { top: 1540px; height: 480px; background: linear-gradient(180deg,#3a2f29,#5a4031 50%,#3a2e28); }
  .section-title { font-size: 34px; font-weight: 300; color: var(--orange); }
  .copy { font-size: 15px; line-height: 1.5; }
  .copy p + p { margin-top: 16px; }
  .phone { border-radius: 26px; background: linear-gradient(165deg,#3a3a3a,#101010); padding: 52px 12px; }
  .phone .screen { width: 100%; height: 100%; border-radius: 4px; }

  /* Achieve */
  .achieve { top: 2020px; height: 580px; background: var(--paper); text-align: center; }
  .achieve .intro { top: 76px; left: 300px; width: 600px; font-size: 14px; line-height: 1.55; color: var(--ink); }
  .achieve .strong { top: 140px; width: 1200px; font-size: 15px; font-weight: 700; color: var(--dark); }
  .perk { width: 240px; display: flex; gap: 18px; align-items: center; text-align: left; font-size: 13px; line-height: 1.4; color: var(--muted); }
  .perk b { color: var(--ink); }

  /* Coming soon */
  .coming { top: 2600px; height: 560px; background: var(--paper); text-align: center; }
  .coming h2 { top: 32px; width: 1200px; font-size: 40px; font-weight: 400; color: var(--dark); letter-spacing: 1px; }
  .coming .lead { top: 96px; left: 100px; width: 1000px; font-size: 13px; line-height: 1.55; color: var(--muted); }
  .stores { top: 168px; left: 520px; display: flex; gap: 34px; }
  .stores span { width: 40px; height: 40px; background: #555; border-radius: 6px; }
  .tablet { top: 232px; left: 260px; width: 680px; height: 330px; border-radius: 30px 30px 0 0; background: #1e1e1e; padding: 26px 26px 0; }
  .tablet .screen { width: 100%; height: 100%; border-radius: 6px 6px 0 0; background: linear-gradient(180deg,#3a3430,#5a4a3e 60%,#2e2a28); }

  /* Notify */
  .notify { top: 3120px; height: 400px; background: linear-gradient(180deg,#2a2624,#3a322c 50%,#262220); text-align: center; color: var(--white); }
  .notify .plane { top: 44px; left: 570px; width: 60px; height: 60px; border-radius: 50%; background: rgba(255,255,255,.12); display: grid; place-items: center; }
  .notify h2 { top: 140px; width: 1200px; font-size: 38px; font-weight: 700; letter-spacing: .5px; }
  .notify .sub { top: 200px; width: 1200px; font-size: 14px; color: #d9d2cc; }
  .signup { top: 258px; left: 264px; width: 672px; height: 56px; display: flex; }
  .signup .field { flex: 1; background: #fff; color: #aaa; font-size: 14px; text-align: left; padding: 18px 22px; }
  .signup .go { width: 150px; background: var(--orange); color: var(--white); font-size: 13px; font-weight: 700; display: grid; place-items: center; }

  /* Footer */
  .site-footer { top: 3520px; height: 116px; background: var(--paper); }
  .site-footer .legal { top: 48px; left: 40px; font-size: 12px; color: var(--muted); }
  .social { top: 40px; left: 976px; display: flex; gap: 10px; }
  .social span { width: 30px; height: 30px; border-radius: 50%; background: #b8b8b8; }
</style>
</head>
<body>

<header class="hero">
  <div class="hero-photo" role="img" aria-label="Friends leaping in the air against a golden sunset"></div>
  <div class="abs brand">Lumora</div>
  <div class="abs tagline">Become a better version of yourself</div>
  <div class="abs contact">
    <span class="dot"><svg width="14" height="14" viewBox="0 0 24 24"><path fill="#f6c500" d="M6.6 10.8a15 15 0 0 0 6.6 6.6l2.2-2.2c.3-.3.7-.4 1-.2 1.1.4 2.3.6 3.6.6.6 0 1 .4 1 1V20c0 .6-.4 1-1 1A17 17 0 0 1 3 4c0-.6.4-1 1-1h3.5c.6 0 1 .4 1 1 0 1.3.2 2.5.6 3.6.1.3 0 .7-.2 1z"/></svg></span>
    +1 555 0148 236
  </div>
  <div class="abs menu-btn"><svg width="26" height="20"><rect y="0" width="26" height="3" fill="#2a2524"/><rect y="8" width="26" height="3" fill="#2a2524"/><rect y="16" width="26" height="3" fill="#2a2524"/></svg></div>
  <svg class="abs arrow" style="left:30px" width="20" height="36"><path d="M16 2 3 18l13 16" stroke="currentColor" stroke-width="3" fill="none"/></svg>
  <svg class="abs arrow" style="left:1150px" width="20" height="36"><path d="M4 2l13 16L4 34" stroke="currentColor" stroke-width="3" fill="none"/></svg>
  <h1 class="abs hero-title">Lumora is a revolutionary &amp; free social platform for collaborative addictions quitting.</h1>
  <div class="abs btn-subscribe">Subscribe</div>
  <div class="abs hero-phone" role="img" aria-label="White smartphone showing the app start screen"></div>
  <div class="abs hero-phone-2" role="img" aria-label="Black smartphone showing the app feed"></div>
  <div class="abs dots"><span></span><span></span></div>
</header>

<section class="features">
  <div class="abs feature" style="left:100px">
    <div class="icon"><svg width="100" height="100" viewBox="0 0 100 100"><circle cx="50" cy="50" r="40" fill="none" stroke="#ffffff" stroke-width="18"/><circle cx="50" cy="50" r="40" fill="none" stroke="#e0402f" stroke-width="18" stroke-dasharray="31 32"/></svg></div>
    <h3>Never be alone</h3>
    <p>Forget what you know - Lumora<br>makes it fun to quit.</p>
  </div>
  <div class="abs feature" style="left:450px">
    <div class="icon"><svg width="100" height="100" viewBox="0 0 100 100"><path d="M50 6l13 30 32 3-24 21 7 32-28-17-28 17 7-32L5 39l32-3z" fill="#f6c500"/></svg></div>
    <h3 class="accent">Network Power</h3>
    <p>Forget what you know - Lumora<br>makes it fun to quit.</p>
  </div>
  <div class="abs feature" style="left:800px">
    <div class="icon"><div role="img" aria-label="Feathered headdress emblem" style="width:100px;height:100px;border-radius:50%;background:radial-gradient(circle,#c9573a,#7a2e22)"></div></div>
    <h3>Stay Motivated</h3>
    <p>Forget what you know - Lumora<br>makes it fun to quit.</p>
  </div>
</section>

<section class="fun">
  <div class="abs phone" style="top:58px;left:238px;width:164px;height:342px"><div class="screen" role="img" aria-label="App screen with hot air balloons at dusk" style="background:linear-gradient(180deg,#2a3c6a,#7a4a6a 60%,#d27a3a)"></div></div>
  <h2 class="abs section-title" style="top:86px;left:650px">Fun</h2>
  <div class="abs copy" style="top:160px;left:480px;width:430px;text-align:center;color:var(--muted)">
    <p>Forget what you know - Lumora makes it fun to quit. The battle between your good and bad demons comes to life in our gamified approach for managing your campaigns.</p>
    <p>Lumora gives you the opportunity to take an active role in helping your network to smash your common addictions as a team. That's right, we converted the cessation process into a social game.</p>
  </div>
</section>

<section class="inspire">
  <h2 class="abs section-title" style="top:94px;left:460px">Inspire</h2>
  <div class="abs copy" style="top:160px;left:300px;width:430px;text-align:center;color:#eee6df">
    <p>Forget what you know - Lumora makes it fun to quit. The battle between your good and bad demons comes to life in our gamified approach for managing your campaigns.</p>
    <p>Lumora gives you the opportunity to take an active role in helping your network to smash your common addictions as a team. That's right, we converted the cessation process into a social game.</p>
  </div>
  <div class="abs phone" style="top:58px;left:780px;width:164px;height:342px"><div class="screen" role="img" aria-label="App screen with a glowing star over stacked coins" style="background:linear-gradient(180deg,#1a3a6a,#2b5b9a 50%,#c99a3a)"></div></div>
</section>

<section class="achieve">
  <h2 class="abs section-title" style="top:0;width:1200px">Achieve</h2>
  <p class="abs intro">Lumora is built as a pyramid of relationships that makes use of the <b>Social Cognitive Theory</b>, to provide a powerful network of positive reinforcement.</p>
  <p class="abs strong">The bigger you make it the stronger you get.</p>
  <div class="abs perk" style="top:220px;left:160px">
    <svg width="56" height="48" viewBox="0 0 56 48"><path d="M2 4h9l7 26h28l6-18H14" fill="none" stroke="#f39a1e" stroke-width="4"/><circle cx="22" cy="40" r="4" fill="#f39a1e"/><circle cx="42" cy="40" r="4" fill="#f39a1e"/></svg>
    <span>Lumora is built as a <b>pyramid relationship</b> that makes use of the <b>Social Cognitive Theory</b></span>
  </div>
  <div class="abs perk" style="top:220px;left:760px">
    <svg width="56" height="48" viewBox="0 0 56 48"><path d="M2 4h9l7 26h28l6-18H14" fill="none" stroke="#f39a1e" stroke-width="4"/><circle cx="22" cy="40" r="4" fill="#f39a1e"/><circle cx="42" cy="40" r="4" fill="#f39a1e"/></svg>
    <span>Lumora is built as a <b>pyramid relationship</b> that makes use of the <b>Social Cognitive Theory</b></span>
  </div>
  <div class="abs perk" style="top:360px;left:160px">
    <svg width="56" height="56" viewBox="0 0 56 56"><circle cx="28" cy="24" r="16" fill="#f39a1e"/><path d="M18 36l-6 18 10-5 6 7 4-18z" fill="#f39a1e"/></svg>
    <span>Lumora is built as a <b>pyramid relationship</b> that makes use of the <b>Social Cognitive Theory</b></span>
  </div>
  <div class="abs perk" style="top:360px;left:760px">
    <svg width="56" height="56" viewBox="0 0 56 56"><circle cx="28" cy="24" r="16" fill="#f39a1e"/><path d="M18 36l-6 18 10-5 6 7 4-18z" fill="#f39a1e"/></svg>
    <span>Lumora is built as a <b>pyramid relationship</b> that makes use of the <b>Social Cognitive Theory</b></span>
  </div>
  <div class="abs phone" style="top:216px;left:518px;width:164px;height:334px"><div class="screen" role="img" aria-label="App screen with a golden trophy" style="background:radial-gradient(circle at 50% 45%,#e0b040,#6a4a1a 70%,#2a1e10)"></div></div>
</section>

<section class="coming">
  <h2 class="abs">COMING SOON</h2>
  <p class="abs lead">Lumora is getting ready for launch. Join a growing circle of people who help each other break old habits, share every small win and keep each other going. Sign up below and be the first to hear when the app opens its doors on your phone, tablet and desktop.</p>
  <div class="abs stores" role="img" aria-label="App store availability"><span></span><span></span><span></span></div>
  <div class="abs tablet"><div class="screen" role="img" aria-label="Tablet showing the app welcome screen with a profile avatar"></div></div>
</section>

<section class="notify">
  <div class="abs plane"><svg width="26" height="26" viewBox="0 0 24 24"><path d="M2 11 22 3l-7 18-3-8z" fill="#fff"/></svg></div>
  <h2 class="abs">GET NOTIFIED OF ANY UPDATES!</h2>
  <p class="abs sub">Subscribe below for the beta release and updates</p>
  <div class="abs signup"><div class="field">Enter your email address</div><div class="go">LET ME KNOW</div></div>
</section>

<footer class="site-footer">
  <p class="abs legal">Copyright © Lumora Ltd. All rights reserved. Contact Us | Terms | Privacy Policy</p>
  <div class="abs social"><span></span><span></span><span></span></div>
</footer>

</body>
</html>
```